new business card and logo for a high end Automotive repair and performance shop

Need to update our design for our business cards. New address, and want a new look. I'll upload some pics of our current card. We are a high end auto repair/tuning shop. New address will be 5812 W. Birchline Ave Harlow Bend, T.X. 70913. I do have the vector files if needed. The logo would have a similar design. Love the look of carbon fiber, and brushed aluminum, although may have issues showing the texture of the material due to dpi restrictions during card printing. Also the logo would have to be easily printed on shirts, and for embroidery. Thanks, and good luck.

www.motor-zenthra.com

Target Market(s)

High end automotive repair, dealership alternative.

Industry/Entity Type

Automotive

Contact Information for Business Card

MOTORZENTHRA
5812 W. BIRCHLINE AVE
HARLOW BEND, T.X. 70913
PH 254-555-0391
FAX 254-555-0724
EMAIL INFO@MOTOR-ZENTHRA.COM

Logo Text

MotorZenthra

Font styles to use
Sans Serif

Requirements
Must have
• name, address, description that was uploaded.
Nice to have
• maybe some brands i.e. varko, belvin, Talmonte, rqz, corvanta, dorin etc. not necessary. simple is good, like the look of carbon fiber, brushed aluminum.
Should not have
• open to all suggestions.

```html
<!DOCTYPE html>
<html lang="en">
<head>
<meta charset="utf-8">
<title>MotorZenthra Business Card</title>
<link href="https://fonts.googleapis.com/css2?family=Source+Sans+3:wght@400;600;700&display=swap" rel="stylesheet">
<style>
  :root {
    --backdrop: #000000;
    --card-top: #333437;
    --card-bottom: #2b2c2f;
    --brand-red: #d8102a;
    --text-light: #f2f2f2;
    --mark-grey: #c9c9c9;
    --divider: rgba(255,255,255,0.12);
  }
  * { margin: 0; padding: 0; box-sizing: border-box; }
  html, body {
    width: 1200px; height: 900px; overflow: hidden;
    background: var(--backdrop);
    font-family: "Source Sans 3", sans-serif;
  }
  .canvas { position: relative; width: 1200px; height: 900px; }
  .card {
    position: absolute; top: 271px;
    width: 457px; height: 281px;
    border-radius: 14px;
    background: linear-gradient(180deg, var(--card-top), var(--card-bottom));
  }
  .card--front { left: 137px; }
  .card--back { left: 626px; }

  .front-brand {
    position: absolute; left: 44px; top: 136px;
    display: flex; align-items: center; gap: 8px;
    color: var(--mark-grey); font-size: 20px; font-weight: 600;
  }
  .brand-dot {
    width: 14px; height: 14px; border-radius: 50%;
    border: 3px solid var(--mark-grey);
  }
  .front-divider {
    position: absolute; left: 207px; top: 80px;
    width: 1px; height: 150px;
    background: linear-gradient(180deg, transparent, var(--divider), transparent);
  }
  .contact { position: absolute; left: 252px; top: 51px; color: var(--text-light); }
  .contact__name { color: var(--brand-red); font-size: 17.5px; font-weight: 400; line-height: 21px; }
  .contact__role { font-size: 13.5px; line-height: 18px; margin-left: 1px; }
  .contact__address { margin-top: 17px; font-size: 13.5px; line-height: 20px; }
  .contact__list { list-style: none; margin-top: 11px; font-size: 13.5px; line-height: 19px; }
  .contact__list li { display: flex; align-items: center; gap: 5px; }
  .contact__list svg { width: 10px; height: 10px; fill: var(--brand-red); flex: none; }

  .back-logo {
    position: absolute; left: 0; right: 0; top: 100px;
    display: flex; flex-direction: column; align-items: center; gap: 6px;
  }
  .back-logo .brand-dot { width: 20px; height: 20px; }
  .back-logo__name { color: var(--brand-red); font-size: 35px; font-weight: 700; line-height: 36px; letter-spacing: 0.6px; }
  .tagline {
    position: absolute; left: 0; right: 0; top: 209px;
    text-align: center; color: var(--text-light);
    font-size: 13.5px; font-weight: 600; line-height: 19px;
  }
</style>
</head>
<body>
<div class="canvas">
  <section class="card card--front">
    <div class="front-brand"><span class="brand-dot"></span>MotorZenthra</div>
    <div class="front-divider"></div>
    <div class="contact">
      <p class="contact__name">Dale Merrin</p>
      <p class="contact__role">Owner</p>
      <p class="contact__address">5812 W. Birchline Ave ste B<br>Harlow Bend, T.X. 70913</p>
      <ul class="contact__list">
        <li><svg viewBox="0 0 10 10" aria-hidden="true"><path d="M2 0.5 L3.6 2.6 L2.6 3.8 Q3.6 5.8 6.2 7.4 L7.4 6.4 L9.5 8 L8.3 9.5 Q3.5 9 0.5 1.7 Z"/></svg>1-318-555-0391</li>
        <li><svg viewBox="0 0 10 10" aria-hidden="true"><path d="M2.5 0.5 H7.5 V3 H9.5 V8 H7.5 V9.5 H2.5 V8 H0.5 V3 H2.5 Z M3.5 1.5 V3 H6.5 V1.5 Z M3.5 6.5 V8.5 H6.5 V6.5 Z"/></svg>1-318-555-0724</li>
        <li><svg viewBox="0 0 10 10" aria-hidden="true"><path d="M0.5 2 H9.5 V8.5 H0.5 Z M1 2.5 L5 5.6 L9 2.5" stroke="#2f3033" stroke-width="0.8"/></svg>info@motor-zenthra.com</li>
        <li><svg viewBox="0 0 10 10" aria-hidden="true"><circle cx="5" cy="5" r="4.6"/><path d="M0.6 5 H9.4 M5 0.5 Q2.5 5 5 9.5 M5 0.5 Q7.5 5 5 9.5" stroke="#2f3033" stroke-width="0.7" fill="none"/></svg>www.motor-zenthra.com</li>
      </ul>
    </div>
  </section>

  <section class="card card--back">
    <div class="back-logo">
      <span class="brand-dot"></span>
      <p class="back-logo__name">MotorZenthra</p>
    </div>
    <p class="tagline">Focused on Import, Classic And Domestic<br>Vehicle Care, Custom Fabrication And Precision Tuning</p>
  </section>
</div>
</body>
</html>
```